Harlow Hauling | ||
Fine furniture transport and delivery service | ||
Use same font as used in my logo | ||
Cutting-Edge Modern Bright & Fun-filled |
Danny Crebbe | ||
Owner | ||
5810 County Road 7 Marlowe,VT 03598 |
pinecarrier@velmorapost.net | ||
Looking for something that stands out. Maybe photo shop my logo into a 2008 or newer Korvath trekline van. | ||

```html
<!DOCTYPE html>
<html lang="en">
<head>
<meta charset="utf-8">
<title>Harlow Hauling – Business Card</title>
<link rel="stylesheet" href="https://fonts.googleapis.com/css2?family=Arimo:ital,wght@0,700;1,400&family=Tinos:wght@400&display=swap">
<style>
  :root {
    --stage: #2b2b2b;
    --card-light: #ffffff;
    --card-shade: #dcdcdc;
    --brand-green: #2fc21c;
    --brand-green-dark: #1e9a10;
    --swoosh-grey: #6e6e6e;
    --ink: #333333;
    --ink-soft: #7a7a7a;
    --rule: #c8c8c8;
  }
  * { margin: 0; padding: 0; box-sizing: border-box; }
  html, body { width: 1200px; height: 901px; overflow: hidden; background: var(--stage); }
  .canvas { position: relative; width: 1200px; height: 901px; }
  .card {
    position: absolute; left: 100px; top: 165px; width: 1000px; height: 571px;
    background: radial-gradient(ellipse at 45% 35%, var(--card-light) 0%, #f3f3f3 55%, var(--card-shade) 100%);
    overflow: hidden; box-shadow: 0 20px 50px rgba(0,0,0,.5);
  }
  .swooshes { position: absolute; left: 0; top: 0; width: 1000px; height: 571px; }
  .brand { position: absolute; left: 140px; top: 78px; display: flex; align-items: center; gap: 26px; }
  .brand-dot { width: 96px; height: 96px; border-radius: 50%; background: var(--brand-green); flex: none; }
  .brand-name {
    font-family: "Tinos", serif; font-weight: 400; font-size: 52px;
    color: var(--brand-green); text-transform: uppercase; letter-spacing: 1px; line-height: 1;
  }
  .brand-tagline {
    font-family: "Tinos", serif; font-size: 15px; color: var(--ink-soft);
    margin-top: 8px; letter-spacing: .5px;
  }
  .person { position: absolute; left: 130px; top: 250px; width: 330px; text-align: center; }
  .person-name { font-family: "Arimo", sans-serif; font-weight: 700; font-size: 31px; color: var(--brand-green-dark); }
  .person-role { font-family: "Arimo", sans-serif; font-style: italic; font-size: 22px; color: var(--ink); margin-top: 2px; }
  .person-address { font-family: "Tinos", serif; font-size: 25px; color: var(--ink); margin-top: 8px; line-height: 1.2; }
  .divider { position: absolute; left: 470px; top: 215px; width: 1px; height: 175px; background: var(--rule); }
  .contacts { position: absolute; left: 500px; top: 222px; font-family: "Tinos", serif; font-size: 24px; color: var(--ink); }
  .contact-line { display: flex; align-items: center; gap: 12px; height: 34px; }
  .contact-icon { width: 24px; height: 24px; flex: none; }
</style>
</head>
<body>
<div class="canvas">
  <div class="card">
    <svg class="swooshes" viewBox="0 0 1000 571" aria-hidden="true">
      <path d="M0 482 C 300 482, 650 425, 1000 310 L 1000 338 C 650 452, 300 502, 0 502 Z" fill="var(--swoosh-grey)"/>
      <path d="M0 507 C 320 512, 680 460, 1000 352 L 1000 571 L 0 571 Z" fill="var(--brand-green)"/>
      <path d="M0 540 C 320 545, 680 495, 1000 405 L 1000 571 L 0 571 Z" fill="var(--brand-green-dark)" opacity=".35"/>
    </svg>

    <div class="brand">
      <div class="brand-dot"></div>
      <div>
        <div class="brand-name">Harlow Hauling</div>
        <div class="brand-tagline">Fine furniture transport and delivery service</div>
      </div>
    </div>

    <div class="person">
      <div class="person-name">Danny Crebbe</div>
      <div class="person-role">Owner</div>
      <div class="person-address">5810 County Road 7<br>Marlowe,VT 03598</div>
    </div>

    <div class="divider"></div>

    <div class="contacts">
      <div class="contact-line">
        <svg class="contact-icon" viewBox="0 0 24 24"><rect x="6" y="2" width="12" height="20" rx="2" fill="var(--brand-green)"/><rect x="8" y="5" width="8" height="11" fill="#fff"/></svg>
        603-555-0148
      </div>
      <div class="contact-line">
        <svg class="contact-icon" viewBox="0 0 24 24"><rect x="6" y="2" width="12" height="20" rx="2" fill="var(--swoosh-grey)"/><rect x="8" y="5" width="8" height="11" fill="#fff"/></svg>
        603-555-0172
      </div>
      <div class="contact-line">
        <svg class="contact-icon" viewBox="0 0 24 24"><circle cx="12" cy="12" r="10" fill="var(--brand-green)"/><text x="12" y="17" text-anchor="middle" font-size="14" font-family="Arimo, sans-serif" font-weight="700" fill="#fff">@</text></svg>
        pinecarrier@velmorapost.net
      </div>
    </div>
  </div>
</div>
</body>
</html>
```